Double-sided business card needed - specific brief

We need a double sided business card designed for our company Radiant Trimline. Having lost a lot of weight myself, the back of the card needs to show my before and after pictures. It needs to cover the entire back side of the card. This might be with my two before pictures over set on top of my main after picture or in separate frames. I'll leave that to your artistic consideration. The front needs to have our logo with contact details centred below.

The cards will be printed by PRINTKO.com and will be rectangular, 84mm x 55mm, but with ROUNDED edges. Please therefore present your designs rectangular but with rounded edges if possible.

The card should be designed in LANDSCAPE orientation.

As well as the logo, the front of the card should have the following details:

Moira Blakewell
Weight Loss Motivator with 189lb personal loss
moira@radiant-trimline.example
+44 (0)7700 900418

The website is important so should perhaps be more bold than the rest:
www.radiant-trimline.example

My brand colours are: Pink #CD2366, Light Pink #FD88AD. Blue #1C9CB1, Light Blue #64C4DE

Target Market(s)

Women 30+

Contact Information for Business Card

As description above

Font styles to use
Sans Serif

Requirements
Must have
• Double sided.
• Back side entirely covered with my before and after pictures.
• You may wish to float my before pictures on top of my after picture or add them in different frames. I look forward to seeing your different suggestions.

```html
<!DOCTYPE html>
<html lang="en">
<head>
<meta charset="utf-8">
<title>Radiant Trimline – Business Card</title>
<link rel="stylesheet" href="https://fonts.googleapis.com/css2?family=Merriweather:wght@400;700&family=Lato:wght@400&display=swap">
<style>
  :root {
    --pink: #CD2366;
    --pink-light: #FD88AD;
    --blue: #1C9CB1;
    --blue-light: #64C4DE;
    --ink: #2b2b2b;
    --stage: #2c2c2c;
    --paper: #ffffff;
  }
  * { box-sizing: border-box; margin: 0; padding: 0; }
  html, body { width: 1200px; height: 802px; overflow: hidden; }
  body { background: var(--stage); position: relative; font-family: "Lato", sans-serif; }

  .card {
    position: absolute;
    top: 274px;
    width: 441px;
    height: 264px;
    border-radius: 9px;
    overflow: hidden;
    background: var(--paper);
  }
  .card--front { left: 136px; }
  .card--back { left: 624px; display: flex; }

  .brand {
    position: absolute;
    left: 0; width: 220px;
    top: 96px;
    display: flex; flex-direction: column; align-items: center; gap: 12px;
  }
  .brand__dot { width: 34px; height: 34px; border-radius: 50%; background: var(--pink); }
  .brand__name {
    font-family: "Merriweather", serif;
    font-weight: 400;
    font-size: 17px;
    letter-spacing: 0.5px;
    color: var(--pink);
    text-transform: uppercase;
    text-align: center;
    line-height: 1.25;
  }

  .divider {
    position: absolute; left: 220px; top: 86px;
    width: 1px; height: 91px; background: #9a9a9a;
  }

  .contact { position: absolute; left: 234px; top: 75px; color: var(--ink); }
  .contact__name {
    font-family: "Merriweather", serif; font-weight: 700; font-size: 16px;
    text-transform: uppercase; letter-spacing: 0.2px; line-height: 1.2;
  }
  .contact__first { color: var(--pink); }
  .contact__last { color: var(--blue); }
  .contact__role { font-size: 12px; line-height: 16px; margin-top: 2px; }
  .contact__lines { margin-top: 15px; font-size: 11.5px; line-height: 16.5px; }
  .contact__line { display: flex; align-items: center; gap: 3px; }
  .contact__line svg { width: 10px; height: 10px; flex: none; }

  .web-band {
    position: absolute; left: 0; right: 0; bottom: 0; height: 45px;
    background: linear-gradient(90deg, var(--pink) 0%, #8f5a8f 50%, #3fafc4 100%);
    display: flex; align-items: center; justify-content: center;
    color: #fff; font-size: 18px; letter-spacing: 0.2px;
  }

  .photo { flex: 1; height: 100%; }
  .photo--before { background: linear-gradient(180deg, #6d8a5a 0%, #a9a07a 30%, #e9e6e0 55%, #6f9a4a 100%); }
  .photo--after { background: linear-gradient(135deg, #d8cfc0 0%, #b79a7a 40%, #2b3350 70%, #34477a 100%); }
</style>
</head>
<body>
  <section class="card card--front" aria-label="Business card front">
    <div class="brand">
      <div class="brand__dot"></div>
      <div class="brand__name">Radiant Trimline</div>
    </div>
    <div class="divider"></div>
    <div class="contact">
      <div class="contact__name"><span class="contact__first">Moira</span> <span class="contact__last">Blakewell</span></div>
      <p class="contact__role">Weight Loss Motivator with<br>189lb personal loss</p>
      <div class="contact__lines">
        <div class="contact__line">
          <svg viewBox="0 0 10 10" aria-hidden="true"><path d="M1 3 Q5 0 9 3 L8 4.5 L6.5 3.8 L6.5 3 Q5 2.6 3.5 3 L3.5 3.8 L2 4.5 Z M2.5 5 H7.5 L8.5 9 H1.5 Z" fill="var(--pink)"/></svg>
          <span>+44 (0)7700 900418</span>
        </div>
        <div class="contact__line">
          <svg viewBox="0 0 10 10" aria-hidden="true"><rect x="1" y="2" width="8" height="6" fill="var(--pink)"/><path d="M1 2 L5 5.5 L9 2" stroke="#fff" stroke-width="0.9" fill="none"/></svg>
          <span>moira@radiant-trimline.example</span>
        </div>
      </div>
    </div>
    <div class="web-band">www.radiant-trimline.example</div>
  </section>

  <section class="card card--back" aria-label="Business card back">
    <div class="photo photo--before" role="img" aria-label="Before photo: Moira outdoors in a garden holding a cat"></div>
    <div class="photo photo--after" role="img" aria-label="After photo: Moira seated on a leather sofa at home"></div>
  </section>
</body>
</html>
```